Seven nights at the harbour

Creation of the cover for the book: "Sept nuits sur le quai du port" with the joined photo of a 70 years old lady.
Title: "Seven nights along the old harbour"
Author: "Mireille Vaston"
Publisher: "Editions Morvane" (should be at the bottom of the page)
Format: 14 x 20.5 cm
The story: A senior lady (70 years old), divorced, with a beautiful face, still wants to seduce, even young men.
We found the perfect photo for the woman. We would like to ask you to make a modern cover from it.
Besoin de quelques jours pour choisir un design
Target Market(s)
Novels reader (adults)
Industry/Entity Type
book

```html
<!DOCTYPE html>
<html lang="en">
<head>
<meta charset="utf-8">
<title>Seven nights along the old harbour — Mireille Vaston</title>
<link rel="stylesheet" href="https://fonts.googleapis.com/css2?family=Bodoni+Moda:wght@600;700&family=Sue+Ellen+Francisco&family=Arvo:wght@700&display=swap">
<style>
  :root {
    --hair-highlight: #e4e6ec;
    --hair-light: #b9bcc6;
    --hair-mid: #8f939e;
    --hair-dark: #575b66;
    --hair-deep: #3f434d;
    --skin-warm: #b0928a;
    --lip-rose: #b98a8e;
    --author-cream: #fbfbe2;
    --script-yellow: #f7f29c;
    --title-pink: #fcc8f8;
    --publisher-white: #ffffff;
  }
  html, body {
    margin: 0;
    padding: 0;
    overflow: hidden;
    background: #ffffff;
  }
  .cover {
    position: relative;
    width: 820px;
    height: 1200px;
    overflow: hidden;
    font-family: "Bodoni Moda", serif;
  }
  .cover-photo {
    position: absolute;
    inset: 0;
    background:
      radial-gradient(ellipse 9% 4% at 60% 46%, var(--lip-rose) 0%, rgba(185,138,142,0) 100%),
      radial-gradient(ellipse 20% 22% at 58% 47%, var(--skin-warm) 0%, rgba(176,146,138,0) 100%),
      radial-gradient(ellipse 45% 18% at 40% 22%, var(--hair-highlight) 0%, rgba(228,230,236,0) 100%),
      radial-gradient(ellipse 30% 14% at 25% 62%, rgba(228,230,236,0.55) 0%, rgba(228,230,236,0) 100%),
      radial-gradient(ellipse 35% 25% at 15% 85%, rgba(63,67,77,0.7) 0%, rgba(63,67,77,0) 100%),
      radial-gradient(ellipse 40% 30% at 90% 80%, rgba(63,67,77,0.6) 0%, rgba(63,67,77,0) 100%),
      linear-gradient(170deg, var(--hair-light) 0%, var(--hair-mid) 40%, var(--hair-dark) 75%, var(--hair-mid) 100%);
  }
  .author {
    position: absolute;
    top: 56px;
    left: 0;
    width: 100%;
    margin: 0;
    text-align: center;
    font-weight: 600;
    font-size: 70px;
    line-height: 1;
    letter-spacing: 1px;
    color: var(--author-cream);
  }
  .title {
    margin: 0;
    font-weight: 400;
  }
  .title-script {
    position: absolute;
    top: 796px;
    left: 0;
    width: 100%;
    text-align: center;
    font-family: "Sue Ellen Francisco", cursive;
    font-size: 84px;
    line-height: 1;
    color: var(--script-yellow);
    padding-left: 16px;
    box-sizing: border-box;
  }
  .title-main {
    position: absolute;
    top: 882px;
    left: 0;
    width: 100%;
    text-align: center;
    font-family: "Arvo", serif;
    font-weight: 700;
    font-size: 126px;
    line-height: 1;
    letter-spacing: 2px;
    color: var(--title-pink);
  }
  .publisher {
    position: absolute;
    top: 1102px;
    left: 0;
    width: 100%;
    margin: 0;
    text-align: center;
    font-weight: 600;
    font-size: 42px;
    line-height: 1;
    letter-spacing: 1px;
    color: var(--publisher-white);
  }
</style>
</head>
<body>
  <main class="cover">
    <div class="cover-photo" role="img" aria-label="Close portrait photograph of a seventy-year-old woman whose windswept silver-grey hair covers most of her face, leaving only her lips visible"></div>
    <p class="author">Mireille Vaston</p>
    <h1 class="title">
      <span class="title-script">Seven nights along the old</span>
      <span class="title-main">HARBOUR</span>
    </h1>
    <p class="publisher">Editions Morvane</p>
  </main>
</body>
</html>
```